Brightpath Dental Studio

Please go to www.brightpathdentalstudio.example and obtain the current company logo.
Doctors name are
Marita Velbonne, DDS
Denis Kalb, DMD
Addresses are
318 Larchmont Ave
Teaneck, NJ 07666
201-555-0147
And
872 14th St.
West New York, NJ 07093
201-555-0182
Theme of the business card should feel modrrn and similar to the website.
Front side should include company logo, doctors name, addresses, phone numbers.
Back of the card should include blank lines for patient's name. Date and time for next scheduled appointment. And notice of 24-hr cancellation courtesy policy.
Dental

```html
<!DOCTYPE html>
<html lang="en">
<head>
<meta charset="utf-8">
<title>Brightpath Dental Studio – Business Card</title>
<link href="https://fonts.googleapis.com/css2?family=Source+Sans+3:wght@400;600&family=Roboto+Condensed:ital,wght@0,400;0,500;1,400&display=swap" rel="stylesheet">
<style>
  :root {
    --paper: #ffffff;
    --ink: #231f20;
    --rule: #8c8c8c;
    --brand-dot: #4a7fb5;
  }
  * { margin: 0; padding: 0; box-sizing: border-box; }
  html, body {
    width: 1200px;
    height: 468px;
    overflow: hidden;
    background: var(--paper);
  }
  .card-sheet {
    position: relative;
    width: 1200px;
    height: 468px;
    background: var(--paper);
    color: var(--ink);
  }

  /* Front */
  .front {
    font-family: "Source Sans 3", sans-serif;
    font-size: 21px;
    line-height: 28px;
  }
  .front-rule {
    position: absolute;
    left: 46px;
    top: 53px;
    width: 465px;
    height: 1px;
    background: var(--ink);
  }
  .doctors {
    position: absolute;
    left: 54px;
    top: 57px;
  }
  .office-teaneck {
    position: absolute;
    left: 359px;
    top: 57px;
    font-style: normal;
  }
  .office-westny {
    position: absolute;
    left: 54px;
    top: 232px;
    font-style: normal;
  }
  .brand {
    position: absolute;
    left: 310px;
    top: 196px;
    transform: translate(-50%, -50%);
    display: flex;
    align-items: center;
    gap: 10px;
    white-space: nowrap;
  }
  .brand-dot {
    width: 14px;
    height: 14px;
    border-radius: 50%;
    background: var(--brand-dot);
  }
  .brand-name {
    font-family: "Source Sans 3", sans-serif;
    font-weight: 600;
    font-size: 24px;
    color: var(--ink);
  }

  /* Back */
  .back {
    position: absolute;
    left: 668px;
    top: 60px;
    width: 464px;
    font-family: "Roboto Condensed", sans-serif;
  }
  .back-title {
    font-size: 28px;
    font-weight: 500;
    line-height: 36px;
    letter-spacing: -0.3px;
  }
  .appt-fields {
    margin-top: 20px;
  }
  .appt-row {
    position: relative;
    height: 38px;
    border-bottom: 1px solid var(--rule);
    font-size: 19px;
    font-style: italic;
  }
  .appt-row .label {
    position: absolute;
    left: 0;
    bottom: 5px;
  }
  .appt-row .label-time {
    left: 235px;
  }
  .appt-notice {
    margin-top: 24px;
    text-align: center;
    font-size: 19px;
    font-style: italic;
    line-height: 29px;
    letter-spacing: -0.3px;
  }
</style>
</head>
<body>
  <main class="card-sheet">
    <section class="front">
      <div class="front-rule"></div>
      <div class="doctors">
        <p>Marita Velbonne, DDS</p>
        <p>Denis Kalb, DMD</p>
      </div>
      <address class="office-teaneck">
        <p>318 Larchmont Ave</p>
        <p>Teaneck, NJ 07666</p>
        <p>201-555-0147</p>
      </address>
      <div class="brand">
        <span class="brand-dot"></span>
        <span class="brand-name">Brightpath Dental Studio</span>
      </div>
      <address class="office-westny">
        <p>872 14th St.</p>
        <p>West New York, NJ 07093</p>
        <p>201-555-0182</p>
      </address>
    </section>

    <section class="back">
      <h2 class="back-title">Appointment</h2>
      <div class="appt-fields">
        <div class="appt-row"><span class="label">Name:</span></div>
        <div class="appt-row"><span class="label">Date:</span><span class="label label-time">Time:</span></div>
        <div class="appt-row"><span class="label">Location:</span></div>
      </div>
      <p class="appt-notice">If you are unable to keep your appointment, please<br>contact us at least 24 hours in advance.</p>
    </section>
  </main>
</body>
</html>
```